Ridgeline Crude Advisors needs a logo design and business card layout.

RCA is a consulting firm in oil and gas, specializing in upstream engineering and field work. We provide engineering solutions for the complete wellbore cycle from casing design to flowback. This includes completion and production design. On-site job supervision and project engineering for conventional and unconventional reservoirs. Asset analysis by reviewing operational conditions of asset packages to determine value of potential acquisitions or divesture.

```html
<!DOCTYPE html>
<html lang="en">
<head>
<meta charset="utf-8">
<title>Ridgeline Crude Advisors – Business Card</title>
<link href="https://fonts.googleapis.com/css2?family=Exo+2:wght@700;800&family=Arimo:wght@400&display=swap" rel="stylesheet">
<style>
  :root {
    --stage: #262626;
    --card: #121212;
    --card-edge: #1c1c1c;
    --gold: #d9b52a;
    --gold-light: #e6cf4a;
    --white: #f2f2f2;
    --grey: #bdbdbd;
  }
  * { margin: 0; padding: 0; box-sizing: border-box; }
  html, body {
    width: 1200px; height: 1200px; overflow: hidden;
    background: var(--stage);
  }
  .stage {
    position: relative; width: 1200px; height: 1200px;
  }
  .card {
    position: absolute; left: 170px;
    width: 860px; height: 491px;
    background: linear-gradient(160deg, var(--card-edge), var(--card) 60%);
    border-radius: 22px;
    box-shadow: 0 14px 30px rgba(0,0,0,.55);
    color: var(--white);
    font-family: "Arimo", Arial, sans-serif;
  }
  .card--back { top: 85px; }
  .card--front { top: 625px; }

  .brand {
    display: flex; align-items: center; gap: 18px;
  }
  .brand__dot {
    width: 58px; height: 58px; border-radius: 50%;
    background: var(--gold); flex-shrink: 0;
  }
  .brand__name {
    font-family: "Exo 2", Arial, sans-serif;
    font-weight: 800; color: var(--gold);
    text-transform: uppercase; line-height: 1.05;
    letter-spacing: 1px;
  }
  .card--back .brand {
    position: absolute; left: 0; right: 0; top: 170px;
    justify-content: center;
  }
  .card--back .brand__name { font-size: 44px; }
  .tagline {
    position: absolute; left: 0; right: 0; bottom: 46px;
    text-align: center; font-size: 17px; color: var(--white);
    letter-spacing: .3px;
  }

  .card--front .brand {
    position: absolute; left: 60px; top: 52px;
  }
  .card--front .brand__name { font-size: 40px; }

  .person {
    position: absolute; left: 70px; top: 190px;
  }
  .person__name {
    font-family: "Exo 2", Arial, sans-serif; font-weight: 800;
    font-size: 27px; letter-spacing: 2px; text-transform: uppercase;
  }
  .person__role {
    font-family: "Exo 2", Arial, sans-serif; font-weight: 800;
    font-size: 20px; letter-spacing: 1.5px; color: var(--gold);
    margin-top: 2px;
  }
  .divider {
    position: absolute; left: 60px; right: 70px; top: 278px;
    height: 2px; background: var(--white);
  }
  .contact {
    position: absolute; left: 60px; top: 300px;
    list-style: none; font-size: 21px; line-height: 36px;
  }
  .contact li { display: flex; align-items: center; gap: 14px; }
  .contact svg { width: 22px; height: 22px; fill: none; stroke: var(--gold-light); stroke-width: 1.8; }
  .address {
    position: absolute; right: 70px; top: 318px;
    text-align: right; font-size: 22px; line-height: 32px;
  }
</style>
</head>
<body>
<main class="stage">

  <section class="card card--back">
    <div class="brand">
      <span class="brand__dot"></span>
      <span class="brand__name">Ridgeline Crude Advisors</span>
    </div>
    <p class="tagline">We provide engineering solutions for the complete wellbore cycle from casing design to flowback.</p>
  </section>

  <section class="card card--front">
    <div class="brand">
      <span class="brand__dot"></span>
      <span class="brand__name">Ridgeline Crude<br>Advisors</span>
    </div>

    <div class="person">
      <p class="person__name">Marcus Delaney</p>
      <p class="person__role">CEO/FOUNDER</p>
    </div>

    <div class="divider"></div>

    <ul class="contact">
      <li>
        <svg viewBox="0 0 24 24"><path d="M6 3h3l2 5-2.5 1.5a11 11 0 0 0 6 6L16 13l5 2v3a2 2 0 0 1-2 2A17 17 0 0 1 4 5a2 2 0 0 1 2-2z"/></svg>
        (555) 214 7780
      </li>
      <li>
        <svg viewBox="0 0 24 24"><rect x="3" y="5" width="18" height="14" rx="1"/><path d="M3 6l9 7 9-7"/></svg>
        marcus@ridgelinecrude.com
      </li>
      <li>
        <svg viewBox="0 0 24 24"><circle cx="12" cy="12" r="9"/><path d="M3 12h18M12 3c3 3 3 15 0 18M12 3c-3 3-3 15 0 18"/></svg>
        www.ridgelinecrude.com
      </li>
    </ul>

    <address class="address" style="font-style:normal">
      1187 Cedar Hollow Road<br>
      Fairview Springs, WI 54021
    </address>
  </section>

</main>
</body>
</html>
```